Crestline Gas and Plumbing Business Card Design

I am after a business card design for my plumbing business called 'Crestline Gas & Plumbing'. I do all types of plumbing and gas work and specialise in general maintenance plumbing. Would like to see designs using current logo

Industry/Entity Type

Plumbing

Contact Information for Business Card

Name - Dale Whitcombe
Phone number - 0455163027
Email - admin@crestlinegasandplumbing.example.com.au
ABN - 68204915336

```html
<!DOCTYPE html>
<html lang="en">
<head>
<meta charset="utf-8">
<title>Crestline Gas &amp; Plumbing – Business Card</title>
<link rel="stylesheet" href="https://fonts.googleapis.com/css2?family=Open+Sans:wght@400;600;800&display=swap">
<style>
  :root {
    --stage: #2a2b2d;
    --blue-light: #4a7ff0;
    --blue-mid: #1f6fce;
    --blue-deep: #2b3f9f;
    --grey-band: #9a9ca0;
    --white: #ffffff;
    --ink: #3a3a3a;
    --rule: #c9c9c9;
    --accent-orange: #f28a1e;
  }
  * { box-sizing: border-box; margin: 0; padding: 0; }
  html, body {
    width: 1200px; height: 885px; overflow: hidden;
    background: var(--stage);
    font-family: "Open Sans", Arial, sans-serif;
  }
  .canvas { position: relative; width: 1200px; height: 885px; }

  .card {
    position: absolute;
    width: 600px; height: 343px;
    border-radius: 2px;
    overflow: hidden;
    box-shadow: 0 14px 30px rgba(0,0,0,.45);
  }

  /* Front */
  .card-front {
    left: 300px; top: 60px;
    background: radial-gradient(circle at 45% 55%, var(--blue-mid) 0%, var(--blue-deep) 85%);
  }
  .card-front::before {
    content: ""; position: absolute; inset: 0;
    background: linear-gradient(115deg, rgba(90,140,245,.55) 0%, rgba(31,111,206,0) 45%);
  }
  .front-brand {
    position: absolute; left: 0; right: 0; top: 118px;
    display: flex; align-items: center; justify-content: center; gap: 12px;
    color: var(--white); font-weight: 800; font-size: 30px; letter-spacing: .5px;
  }
  .brand-dot {
    width: 22px; height: 22px; border-radius: 50%;
    background: var(--accent-orange); flex: none;
  }
  .front-url {
    position: absolute; left: 0; right: 0; bottom: 62px;
    text-align: center; color: var(--white);
    font-size: 14px; letter-spacing: 3px; font-weight: 400;
  }

  /* Back */
  .card-back {
    left: 300px; top: 470px;
    background: var(--white);
  }
  .name-band {
    position: absolute; left: 0; top: 0; width: 100%; height: 62px;
    background: linear-gradient(90deg, var(--blue-deep), var(--blue-mid) 60%, var(--blue-deep));
  }
  .shade-band {
    position: absolute; left: 0; top: 62px; width: 100%; height: 22px;
    background: linear-gradient(180deg, var(--grey-band), #e6e6e6);
  }
  .holder-name {
    position: absolute; left: 160px; top: 16px;
    color: var(--white); font-weight: 800; font-size: 24px;
  }
  .corner-mark {
    position: absolute; left: 22px; top: 94px;
    width: 26px; height: 26px; border-radius: 50%;
    background: var(--grey-band);
  }
  .back-brand {
    position: absolute; left: 36px; top: 196px; width: 215px;
    display: flex; align-items: center; gap: 12px;
    color: var(--blue-deep); font-weight: 800; font-size: 20px; line-height: 24px;
  }
  .back-brand .brand-dot { width: 20px; height: 20px; }
  .divider {
    position: absolute; left: 268px; top: 104px;
    width: 1px; height: 140px; background: var(--rule);
  }
  .contact-list {
    position: absolute; left: 282px; top: 110px;
    list-style: none; color: var(--ink);
    font-size: 11px; line-height: 25px;
  }
  .contact-list li { display: flex; align-items: center; gap: 8px; white-space: nowrap; }
  .contact-list svg { width: 13px; height: 13px; flex: none; fill: var(--blue-mid); }
  .contact-list .no-icon { padding-left: 21px; }
</style>
</head>
<body>
<main class="canvas">

  <section class="card card-front" aria-label="Card front">
    <div class="front-brand"><span class="brand-dot"></span><span>Crestline Gas &amp; Plumbing</span></div>
    <p class="front-url">www.crestlinegasandplumbing.example.com.au</p>
  </section>

  <section class="card card-back" aria-label="Card back">
    <div class="name-band"></div>
    <div class="shade-band"></div>
    <h1 class="holder-name">Dale Whitcombe</h1>
    <span class="corner-mark"></span>

    <div class="back-brand"><span class="brand-dot"></span><span>Crestline<br>Gas &amp; Plumbing</span></div>

    <span class="divider"></span>
    <ul class="contact-list">
      <li>
        <svg viewBox="0 0 24 24" aria-hidden="true"><path d="M6.6 10.8a15 15 0 0 0 6.6 6.6l2.2-2.2c.3-.3.7-.4 1-.2 1.1.4 2.3.6 3.6.6.6 0 1 .4 1 1V20c0 .6-.4 1-1 1A17 17 0 0 1 3 4c0-.6.4-1 1-1h3.5c.6 0 1 .4 1 1 0 1.3.2 2.5.6 3.6.1.3 0 .7-.2 1z"/></svg>
        0455163027
      </li>
      <li>
        <svg viewBox="0 0 24 24" aria-hidden="true"><path d="M2 5h20v14H2z M2 5l10 8 10-8" fill="none" stroke="#1f6fce" stroke-width="2"/></svg>
        admin@crestlinegasandplumbing.example.com.au
      </li>
      <li>
        <svg viewBox="0 0 24 24" aria-hidden="true"><circle cx="12" cy="12" r="10"/><path d="M2 12h20M12 2c3 3 3 17 0 20M12 2c-3 3-3 17 0 20" fill="none" stroke="#fff" stroke-width="1.5"/></svg>
        crestlinegasandplumbing.example.com.au
      </li>
      <li class="no-icon">ABN - 68204915336</li>
    </ul>
  </section>

</main>
</body>
</html>
```